Energy drink company looking for a complete can design

Design an energy drink can label using an established trademarked logo along with mandatory nutrition and ingredients table.
We would like to see 3 versions or samples to judge:
1. can design over a black background - called dark color version
2. can design over a white background - called light color version
3. can design over a grey/silver background - called balanced color version

Target Market(s)

USA

Requirements
Must have
• the phrase "yes kelvora energy drink" "yes kelvora" and "ALL Natural Libido Enhancing energy drink" must be on the can somewhere

```html
<!DOCTYPE html>
<html lang="en">
<head>
<meta charset="utf-8">
<title>yes kelvora energy drink – can label range</title>
<link rel="stylesheet" href="https://fonts.googleapis.com/css2?family=Poppins:wght@300;400&display=swap">
<style>
  :root {
    --stage: #d3d3d3;
    --gold-light: #f7efad;
    --gold-mid: #c9a444;
    --gold-deep: #8a6a3e;
    --gold-text: #c8a95a;
    --ink: #111111;
    --dark-top: #050505;
    --dark-side: #3a3a3a;
    --light-top: #ffffff;
    --light-side: #ececec;
    --silver-edge: #8c8c94;
    --silver-mid: #e4e4ea;
    --silver-shadow: #4f4f55;
  }
  * { box-sizing: border-box; margin: 0; padding: 0; }
  html, body { width: 1200px; height: 1200px; overflow: hidden; }
  body {
    background: var(--stage);
    font-family: "Poppins", sans-serif;
    position: relative;
  }
  .label {
    position: absolute;
    top: 186px;
    width: 316px;
    height: 876px;
    text-align: center;
    border-radius: 6px;
    overflow: hidden;
  }
  .label--dark { left: 71px; background: linear-gradient(90deg, var(--dark-top) 0%, var(--dark-top) 30%, var(--dark-side) 75%, var(--dark-top) 100%); }
  .label--light { left: 442px; background: linear-gradient(90deg, var(--light-top) 0%, var(--light-top) 35%, var(--light-side) 100%); }
  .label--balanced { left: 815px; background: linear-gradient(90deg, var(--silver-edge) 0%, var(--silver-mid) 25%, var(--silver-mid) 55%, var(--silver-edge) 85%, var(--silver-shadow) 100%); }

  .brand-name {
    position: absolute;
    top: 170px;
    left: 0; right: 0;
    font-weight: 300;
    font-size: 44px;
    letter-spacing: -0.5px;
    color: var(--gold-text);
  }
  .version-name {
    position: absolute;
    top: 358px;
    left: 0; right: 0;
    font-weight: 300;
    font-size: 31px;
    line-height: 36px;
  }
  .label--dark .version-name { color: var(--gold-text); }
  .label--light .version-name { color: #8a6f45; }
  .label--balanced .version-name { color: #2a2a2e; }

  .claim {
    position: absolute;
    top: 562px;
    left: 0; right: 0;
    font-weight: 300;
    font-size: 18px;
    line-height: 20px;
    letter-spacing: 1.5px;
  }
  .label--dark .claim { color: #9a9a9a; }
  .label--light .claim { color: #7a7a7a; top: 578px; }
  .label--balanced .claim { color: #2a2a2e; top: 578px; }

  .gold-band {
    position: absolute;
    left: 0; right: 0; bottom: 0;
    height: 256px;
    background: linear-gradient(90deg, var(--gold-light) 0%, var(--gold-mid) 40%, var(--gold-deep) 80%, #a58957 100%);
  }
  .energy-badge {
    position: absolute;
    top: 50px;
    left: 50%;
    width: 110px;
    height: 110px;
    margin-left: -55px;
  }
  .volume {
    position: absolute;
    bottom: 26px;
    left: 0; right: 0;
    font-size: 14px;
    color: var(--ink);
  }
</style>
</head>
<body>

  <section class="label label--dark">
    <p class="brand-name">yes kelvora</p>
    <p class="version-name">Called Dark<br>Color Version</p>
    <p class="claim">ALL NATURAL LIBIDO<br>ENHANCING</p>
    <div class="gold-band">
      <svg class="energy-badge" viewBox="0 0 110 110" aria-label="Energy drink badge">
        <defs><path id="ring-dark" d="M55,55 m-42,0 a42,42 0 1,1 84,0 a42,42 0 1,1 -84,0"/></defs>
        <text font-family="Poppins, sans-serif" font-size="11" letter-spacing="3" fill="#111"><textPath href="#ring-dark">ENERGY DRINK • ENERGY DRINK •</textPath></text>
        <path d="M60,28 L42,60 L54,60 L48,86 L68,50 L56,50 Z" fill="#111"/>
      </svg>
      <p class="volume">12fl oz (355 ml)</p>
    </div>
  </section>

  <section class="label label--light">
    <p class="brand-name">yes kelvora</p>
    <p class="version-name">Called Ligth<br>Color Version</p>
    <p class="claim">ALL NATURAL LIBIDO<br>ENHANCING</p>
    <div class="gold-band">
      <svg class="energy-badge" viewBox="0 0 110 110" aria-label="Energy drink badge">
        <defs><path id="ring-light" d="M55,55 m-42,0 a42,42 0 1,1 84,0 a42,42 0 1,1 -84,0"/></defs>
        <text font-family="Poppins, sans-serif" font-size="11" letter-spacing="3" fill="#111"><textPath href="#ring-light">ENERGY DRINK • ENERGY DRINK •</textPath></text>
        <path d="M60,28 L42,60 L54,60 L48,86 L68,50 L56,50 Z" fill="#111"/>
      </svg>
      <p class="volume">12fl oz (355 ml)</p>
    </div>
  </section>

  <section class="label label--balanced">
    <p class="brand-name">yes kelvora</p>
    <p class="version-name">Called Balanced<br>Color Version</p>
    <p class="claim">ALL NATURAL LIBIDO<br>ENHANCING</p>
    <div class="gold-band">
      <svg class="energy-badge" viewBox="0 0 110 110" aria-label="Energy drink badge">
        <defs><path id="ring-balanced" d="M55,55 m-42,0 a42,42 0 1,1 84,0 a42,42 0 1,1 -84,0"/></defs>
        <text font-family="Poppins, sans-serif" font-size="11" letter-spacing="3" fill="#111"><textPath href="#ring-balanced">ENERGY DRINK • ENERGY DRINK •</textPath></text>
        <path d="M60,28 L42,60 L54,60 L48,86 L68,50 L56,50 Z" fill="#111"/>
      </svg>
      <p class="volume">12fl oz (355 ml)</p>
    </div>
  </section>

</body>
</html>
```